Lanternfall Festival 2021

We would like to design a campaign with a great picture of Desmond Harlow Pike, Jr. with a big tear coming out of his eye, that image with the Ballad of the Silver Orchard Tide. With a caption under it that says: America, you are better than this.

```html
<!DOCTYPE html>
<html lang="en">
<head>
<meta charset="utf-8">
<title>Lanternfall Festival 2021</title>
<link rel="stylesheet" href="https://fonts.googleapis.com/css2?family=Roboto+Condensed:ital,wght@0,400;0,700;1,300;1,400&display=swap">
<style>
  :root {
    --ink: #333333;
    --red: #d71920;
    --navy: #141a5e;
    --white: #ffffff;
    --haze-light: #ececec;
    --haze-mid: #d4d4d4;
    --portrait-dark: #2b2b2b;
    --portrait-mid: #6a6a6a;
    --caption-ink: #1e1e1e;
  }
  html, body {
    margin: 0;
    padding: 0;
    overflow: hidden;
    background: var(--white);
  }
  .poster {
    position: relative;
    width: 1200px;
    height: 1200px;
    overflow: hidden;
    font-family: "Roboto Condensed", "Arial Narrow", sans-serif;
    background: var(--haze-light);
  }
  .crowd-backdrop {
    position: absolute;
    inset: 0;
    background:
      radial-gradient(ellipse 70% 40% at 30% 75%, rgba(150,150,150,0.45), transparent 70%),
      linear-gradient(180deg, var(--haze-light) 0%, #e2e2e2 35%, var(--haze-mid) 100%);
  }
  .portrait {
    position: absolute;
    left: 545px;
    top: 60px;
    width: 655px;
    height: 1140px;
    border-radius: 260px 200px 0 0;
    background:
      radial-gradient(ellipse 45% 35% at 45% 32%, #8a8a8a, transparent 75%),
      linear-gradient(180deg, var(--portrait-mid) 0%, var(--portrait-dark) 55%, #3a3a3a 100%);
  }
  .headline {
    position: absolute;
    z-index: 2;
    left: 42px;
    top: 305px;
    width: 480px;
    margin: 0;
    font-weight: 700;
    text-transform: uppercase;
    line-height: 1;
  }
  .headline span { display: block; white-space: nowrap; }
  .headline .name {
    color: var(--ink);
    font-size: 104px;
    letter-spacing: -1px;
    line-height: 0.93;
  }
  .headline .event {
    color: var(--red);
    font-size: 78px;
    margin-top: 30px;
    letter-spacing: -1px;
  }
  .headline .year {
    color: var(--navy);
    font-size: 76px;
    margin-top: 14px;
    letter-spacing: -1px;
  }
  .caption-band {
    position: absolute;
    z-index: 3;
    left: 0;
    top: 983px;
    width: 1200px;
    height: 217px;
  }
  .flag-art {
    position: absolute;
    z-index: 4;
    left: 30px;
    top: 1008px;
    width: 250px;
    height: 176px;
    background: linear-gradient(135deg, #1f2f7a 0%, #1f2f7a 38%, #c8303a 39%, #e9e9e9 60%, #c8303a 80%);
    border-radius: 4px;
  }
  .caption {
    position: absolute;
    z-index: 4;
    left: 322px;
    top: 1056px;
  }
  .caption-title {
    margin: 0;
    color: var(--caption-ink);
    font-weight: 700;
    font-size: 32px;
    text-transform: uppercase;
    line-height: 1;
  }
  .caption-line {
    margin: 14px 0 0;
    color: var(--caption-ink);
    font-style: italic;
    font-weight: 300;
    font-size: 38px;
    line-height: 1;
  }
</style>
</head>
<body>
  <main class="poster">
    <div class="crowd-backdrop" role="img" aria-label="Faded black and white photo of a large crowd gathered outdoors"></div>
    <div class="portrait" role="img" aria-label="Black and white portrait of Desmond Harlow Pike, Jr. with a large tear on his cheek"></div>

    <h1 class="headline">
      <span class="name">Desmond</span>
      <span class="name">Harlow</span>
      <span class="name">Pike, Jr.</span>
      <span class="event">Lanternfall</span>
      <span class="year">Festival 2021</span>
    </h1>

    <svg class="caption-band" viewBox="0 0 1200 217" aria-hidden="true">
      <polygon points="0,0 948,0 878,217 0,217" fill="var(--white)"/>
      <polygon points="942,0 952,0 882,217 872,217" fill="var(--red)"/>
    </svg>

    <div class="flag-art" role="img" aria-label="Waving national flag on a pole"></div>

    <div class="caption">
      <p class="caption-title">Ballad of the Silver Orchard Tide</p>
      <p class="caption-line">America, you are better than this</p>
    </div>
  </main>
</body>
</html>
```